Q5 Pops (CBD candy infused with Delta-8)

The proposed logo are two pool table balls. One is a D and the other is an 8, its a brand and we need a label for Gummy human treats. This treats are being infused with Delt-8. I i will upload examples only. The example is of the type of labels needed (package and label for bottle)

Target Market(s)

Your professionals

Font styles to use
Sans Serif

Requirements
Must have
• Youthful look
Nice to have
• Consider using the Delta symbol instead of the D.
Also, I provided a sample of a label that's used on two type of packages.

```html
<!DOCTYPE html>
<html lang="en">
<head>
<meta charset="UTF-8">
<title>Q5 Pops – CBD + Δ8 Gummies Labels</title>
<link href="https://fonts.googleapis.com/css2?family=Montserrat:wght@700;800&display=swap" rel="stylesheet">
<style>
  :root {
    --page: #ffffff;
    --white: #ffffff;
    --blue: #05a6e6;
    --magenta: #e2118d;
    --orange: #ea4a1f;
    --purple: #a6208f;
    --yellow: #f6e900;
    --pink: #ea1f66;
  }
  * { box-sizing: border-box; margin: 0; padding: 0; }
  html, body { width: 1200px; height: 714px; overflow: hidden; background: var(--page); }
  body { position: relative; font-family: "Montserrat", Arial, sans-serif; }

  .label {
    position: absolute;
    top: 258px;
    width: 326px;
    height: 276px;
    overflow: hidden;
  }
  .label--blue   { left: 61px; }
  .label--purple { left: 454px; }
  .label--pink   { left: 838px; }

  .label__pattern { position: absolute; inset: 0; }
  .label--blue .label__pattern   { background: linear-gradient(135deg, var(--magenta), #c04fb8 50%, var(--magenta)); }
  .label--purple .label__pattern { background: linear-gradient(135deg, var(--orange), #c8345a 50%, var(--orange)); }
  .label--pink .label__pattern   { background: linear-gradient(135deg, var(--yellow), #f58a4a 50%, var(--yellow)); }

  .label__disc {
    position: absolute;
    left: 55px; top: 48px;
    width: 222px; height: 222px;
    border-radius: 50%;
  }
  .label--blue .label__disc   { background: var(--blue); }
  .label--purple .label__disc { background: var(--purple); }
  .label--pink .label__disc   { background: var(--pink); }

  .brand {
    position: absolute;
    left: 0; right: 0; top: 44px;
    display: flex; justify-content: center; align-items: center; gap: 8px;
    color: var(--white);
    font-weight: 800;
    font-size: 28px;
    letter-spacing: 0.5px;
  }
  .brand__dot { width: 14px; height: 14px; border-radius: 50%; background: var(--white); }

  .title {
    position: absolute;
    left: 0; right: 0; top: 118px;
    text-align: center;
    color: var(--white);
    font-weight: 700;
    font-size: 37px;
    line-height: 35px;
  }

  .dose {
    position: absolute;
    left: 0; right: 0; top: 203px;
    display: flex; justify-content: center;
  }
  .dose__item { width: 74px; text-align: center; }
  .dose__item + .dose__item { border-left: 1.5px solid var(--white); }
  .dose__amount { display: block; font-weight: 700; font-size: 16px; line-height: 18px; }
  .dose__unit { display: block; font-weight: 700; font-size: 7.5px; line-height: 10px; }
  .label--blue .dose   { color: var(--magenta); }
  .label--purple .dose { color: var(--orange); }
  .label--pink .dose   { color: var(--yellow); }
</style>
</head>
<body>

  <section class="label label--blue">
    <div class="label__pattern" role="img" aria-label="Decorative blue coral-shape pattern on magenta"></div>
    <div class="label__disc"></div>
    <div class="brand"><span class="brand__dot"></span>Q5 Pops</div>
    <h1 class="title">CBD+Δ8<br>GUMMIES</h1>
    <div class="dose">
      <div class="dose__item"><span class="dose__amount">10mg</span><span class="dose__unit">CBD EACH</span></div>
      <div class="dose__item"><span class="dose__amount">10mg</span><span class="dose__unit">D8 EACH</span></div>
    </div>
  </section>

  <section class="label label--purple">
    <div class="label__pattern" role="img" aria-label="Decorative purple coral-shape pattern on orange"></div>
    <div class="label__disc"></div>
    <div class="brand"><span class="brand__dot"></span>Q5 Pops</div>
    <h1 class="title">CBD+Δ8<br>GUMMIES</h1>
    <div class="dose">
      <div class="dose__item"><span class="dose__amount">10mg</span><span class="dose__unit">CBD EACH</span></div>
      <div class="dose__item"><span class="dose__amount">10mg</span><span class="dose__unit">D8 EACH</span></div>
    </div>
  </section>

  <section class="label label--pink">
    <div class="label__pattern" role="img" aria-label="Decorative pink coral-shape pattern on yellow"></div>
    <div class="label__disc"></div>
    <div class="brand"><span class="brand__dot"></span>Q5 Pops</div>
    <h1 class="title">CBD+Δ8<br>GUMMIES</h1>
    <div class="dose">
      <div class="dose__item"><span class="dose__amount">10mg</span><span class="dose__unit">CBD EACH</span></div>
      <div class="dose__item"><span class="dose__amount">10mg</span><span class="dose__unit">D8 EACH</span></div>
    </div>
  </section>

</body>
</html>
```